Cake-Stealing, Churros and Pushing Your Luck

Looking to get a book cover designed.

I am an entrepreneur with an edge (I am fun, outgoing and with tons of personality) and run a localisation company called Tonglingo. My book is my story, some business lessons and also some language lessons and idioms. I am an entrepreneur who has set up his business in a country other than his, with a different language - and thus my book talks about communication and the problems that do arise when things get lost in translation.

I have included, attached, a document with three forewords/introductions from others about the book.

The title of the book is:

Child-Biting,
Chorizo
and Chancing Your Arm
(whatever that means) [in small letters]

And the subtitle:
How a homesick Spaniard found his feet in Britain

Notes:

I was a child biter
I am from Spain - thus chorizo
And I set a business up in the UK - took a risk "chance my arm"

Also, may be a good idea (depends how it looks) to have "whatever that means" in small letters after chancing your arm, since most English people do not know the meaning of this expression. And I constantly play on words with communication throughout the book.

Style notes:

The book is fun, entertaining and I do not take myself too seriously, so I want the cover to be professional, bold and striking.

I like the colours black and red, but these are not a must. The idea is to make the cover stand out, while still remain professional.

--------
Chancing Your Arm: http://www.brennockabbey.example/chancing-your-arm.aspx

Target Market(s)

Entrepreneurs, business owners, linguists, people that work in large organisations but appreciate a bit of a human/personal touch.

Industry/Entity Type

Business

Font styles to use
Sans Serif
Other font styles liked:
• Modern font.

Colors
ec1f27
ffffff
000000
d5d5d5
0355a3

Requirements
Nice to have
• Bold statement
• Striking but classy
• Fun
• Different
• Stand out
Should not have
• Traditional boring style
• Yellow colour

```html
<!DOCTYPE html>
<html lang="en">
<head>
<meta charset="utf-8">
<title>Cake-Stealing, Churros and Pushing Your Luck – Book Cover</title>
<link rel="stylesheet" href="https://fonts.googleapis.com/css2?family=Oswald:wght@500;600&family=Libre+Baskerville:ital@1&display=swap">
<style>
  :root {
    --red-light: #e3232c;
    --red: #c8161f;
    --red-dark: #8e0d14;
    --white: #ffffff;
    --ink: #1a1a1a;
    --paper-light: #f2f2f2;
    --paper-dark: #cfcfcf;
  }
  html, body {
    margin: 0;
    padding: 0;
    width: 982px;
    height: 1200px;
    overflow: hidden;
    background: var(--white);
  }
  .cover {
    position: relative;
    width: 982px;
    height: 1200px;
    overflow: hidden;
    background: radial-gradient(ellipse 70% 55% at 55% 45%, var(--red-light) 0%, var(--red) 45%, var(--red-dark) 100%);
    font-family: "Oswald", "Arial Narrow", sans-serif;
  }
  .title {
    position: absolute;
    top: 160px;
    left: 0;
    right: 0;
    margin: 0;
    text-align: center;
    color: var(--white);
    font-weight: 500;
    font-size: 112px;
    line-height: 110px;
    text-transform: uppercase;
    letter-spacing: -2px;
  }
  .title .line { display: block; }
  .title .line--small { font-size: 94px; }
  .aside {
    position: absolute;
    top: 548px;
    left: 0;
    right: 0;
    margin: 0;
    text-align: center;
    color: var(--white);
    font-family: "Libre Baskerville", Georgia, serif;
    font-style: italic;
    font-size: 26px;
  }
  .tear {
    position: absolute;
    left: 0;
    top: 610px;
    width: 982px;
    height: 320px;
  }
  .subtitle {
    position: absolute;
    top: 705px;
    left: 0;
    right: 0;
    margin: 0;
    text-align: center;
    color: var(--ink);
    font-weight: 600;
    font-size: 54px;
    line-height: 1.2;
    text-transform: uppercase;
    letter-spacing: 0.5px;
  }
  .author {
    position: absolute;
    top: 1000px;
    left: 0;
    right: 0;
    margin: 0;
    text-align: center;
    color: var(--white);
    font-weight: 500;
    font-size: 56px;
    letter-spacing: 5px;
    text-transform: uppercase;
  }
</style>
</head>
<body>
  <main class="cover">
    <h1 class="title">
      <span class="line">Cake-Stealing,</span>
      <span class="line">Churros and</span>
      <span class="line line--small">Pushing Your Luck</span>
    </h1>
    <p class="aside">(whatever that means)</p>

    <svg class="tear" viewBox="0 0 982 320" aria-hidden="true">
      <defs>
        <linearGradient id="paper" x1="0" y1="0" x2="1" y2="1">
          <stop offset="0" stop-color="var(--paper-dark)"/>
          <stop offset="0.45" stop-color="var(--paper-light)"/>
          <stop offset="1" stop-color="var(--paper-dark)"/>
        </linearGradient>
      </defs>
      <polygon fill="url(#paper)" stroke="#ffffff" stroke-width="3"
        points="0,22 30,16 55,28 90,12 125,24 160,18 195,32 235,22 275,30 310,44 350,36 390,50 425,42 465,56 505,48 545,62 585,56 620,70 660,62 700,78 740,70 780,86 820,78 860,94 900,86 940,100 982,92
                982,300 945,292 910,304 870,290 835,296 795,282 760,290 720,274 685,282 645,266 610,272 570,256 535,262 495,246 460,254 420,238 385,244 345,228 310,236 270,220 235,226 195,210 160,218 120,202 85,210 45,196 0,204"/>
    </svg>

    <p class="subtitle">How a homesick Spaniard<br>found his feet in Britain</p>

    <p class="author">Daniel Ferrer Molina</p>
  </main>
</body>
</html>
```